Teach English in China Website Redesign Needed

We recruit native English speakers from the US, UK, etc. who want to teach English as a foreign language in schools in China. Our target customer is college educated, age 22-28 and they love to travel. We prefer designs with bright colors and lots of photos. We want to keep all the text on our current homepage, LanternClassroomHub.com. We are open to changing our logo. A competitor's page that we like is bluepeakmentors.com because of their bright colors, photos and use of white space. We are happy to give you a dofollow link and design credit on our homepage. The use of included photos is optional. We need at least a home page design and a standard blog post design.
Target Market(s)
Our target customer is college educated, age 22-28 and they love to travel. Half of our customers are kindergarten teachers. Half of our customers are male.
Logo Text
Lantern Classroom Hub
Number of Pages Required
2 page
Requirements
Must have
- Bright colors
Should not have
- Our homepage must not look crowded. Use white space effectively.

```html
<!DOCTYPE html>
<html lang="en">
<head>
<meta charset="utf-8">
<title>Lantern Classroom Hub – Apply and Testimonials</title>
<link rel="stylesheet" href="https://fonts.googleapis.com/css2?family=Questrial&family=Jost:wght@700&family=Chakra+Petch:wght@500&family=Poppins:wght@400;600&family=Mulish:wght@400&display=swap">
<style>
  :root {
    --hero-dark: #3a1a0c;
    --hero-warm: #7a3a14;
    --hero-glow: #a8641e;
    --lime: #c6ff6a;
    --lime-soft: #c8f27a;
    --orange: #ff6a00;
    --ink: #1c1c1c;
    --name-ink: #4a3a38;
    --dot: #a9a9a9;
    --dot-active: #4c8a0c;
    --yellow: #ffff6a;
    --button-ink: #5a7d00;
    --band-dark: #2a2b22;
    --band-green: #3e4a2c;
    --white: #ffffff;
  }
  * { box-sizing: border-box; margin: 0; padding: 0; }
  html, body { width: 1200px; height: 1160px; overflow: hidden; background: var(--white); }
  body { position: relative; font-family: "Mulish", sans-serif; color: var(--ink); }

  .apply-hero {
    position: absolute; left: 0; top: 0; width: 1200px; height: 415px;
    background:
      radial-gradient(ellipse 260px 200px at 540px 330px, rgba(168,100,30,0.75), transparent 70%),
      radial-gradient(ellipse 380px 240px at 950px 300px, rgba(122,58,20,0.6), transparent 75%),
      linear-gradient(180deg, #2e150a 0%, var(--hero-warm) 55%, var(--hero-dark) 100%);
  }
  .apply-hero__note {
    position: absolute; left: 0; width: 1200px; top: 126px;
    text-align: center; color: var(--white);
    font-family: "Questrial", sans-serif; font-size: 27px; line-height: 36px;
  }
  .apply-hero__button {
    position: absolute; left: 453px; top: 236px; width: 238px; height: 60px;
    border-radius: 6px; background: var(--lime);
    display: flex; align-items: center; justify-content: center;
    font-family: "Chakra Petch", sans-serif; font-weight: 500; font-size: 18px; color: var(--ink);
    text-decoration: none;
  }

  .testimonials { position: absolute; left: 0; top: 415px; width: 1200px; height: 556px; }
  .testimonials__title {
    position: absolute; left: 0; width: 1200px; top: 58px; text-align: center;
    font-family: "Jost", sans-serif; font-weight: 700; font-size: 37px; color: var(--orange);
    letter-spacing: 0.5px;
  }
  .testimonials__quote { position: absolute; left: 588px; top: 145px; }
  .testimonials__avatar {
    position: absolute; left: 557px; top: 203px; width: 104px; height: 104px; border-radius: 50%;
    background: radial-gradient(circle at 50% 40%, #6b5848 0%, #2a2420 60%, #111 100%);
  }
  .testimonials__meta {
    position: absolute; left: 0; width: 1200px; top: 319px; text-align: center;
    font-family: "Poppins", sans-serif; font-size: 13.5px; color: var(--name-ink);
  }
  .testimonials__name { font-weight: 600; font-size: 16px; }
  .testimonials__body {
    position: absolute; left: 278px; width: 644px; top: 353px; text-align: center;
    font-size: 13.5px; line-height: 21.3px; color: var(--ink);
  }
  .testimonials__dots { position: absolute; left: 552px; top: 488px; display: flex; gap: 8px; }
  .testimonials__dot { width: 11px; height: 11px; border-radius: 50%; background: var(--dot); }
  .testimonials__dot--active { background: var(--dot-active); }

  .faq-band {
    position: absolute; left: 0; top: 971px; width: 1200px; height: 189px;
    background:
      radial-gradient(ellipse 200px 160px at 600px 150px, rgba(110,90,60,0.7), transparent 75%),
      linear-gradient(90deg, var(--band-green) 0%, var(--band-dark) 50%, #1f221c 100%);
    border-bottom: 2px solid var(--lime-soft);
  }
  .faq-band__text {
    position: absolute; left: 90px; top: 72px;
    font-family: "Questrial", sans-serif; font-size: 31px; color: var(--yellow);
  }
  .faq-band__button {
    position: absolute; left: 926px; top: 71px; width: 159px; height: 51px; border-radius: 6px;
    background: var(--yellow); color: var(--button-ink);
    display: flex; align-items: center; justify-content: center;
    font-family: "Chakra Petch", sans-serif; font-weight: 500; font-size: 17px; text-decoration: none;
  }
</style>
</head>
<body>
  <section class="apply-hero" role="img" aria-label="Photo of a fisherman in a straw hat holding a lantern on a river raft at dusk">
    <p class="apply-hero__note">Please make sure you read our FREQUENTLY ASKED QUESTIONS<br>before submitting your information.</p>
    <a class="apply-hero__button" href="#">Apply now !</a>
  </section>

  <section class="testimonials">
    <h2 class="testimonials__title">TESTIMONIALS</h2>
    <svg class="testimonials__quote" width="42" height="36" viewBox="0 0 42 36" aria-hidden="true">
      <path fill="var(--lime-soft)" d="M0 16 C0 6 6 1 14 0 L15 5 C10 6 8 9 8 14 L18 14 L18 36 L0 36 Z M24 16 C24 6 30 1 38 0 L39 5 C34 6 32 9 32 14 L42 14 L42 36 L24 36 Z"/>
    </svg>
    <div class="testimonials__avatar" role="img" aria-label="Portrait photo of the reviewer"></div>
    <p class="testimonials__meta"><span class="testimonials__name">Leo Hartley,</span> January 2, 2017</p>
    <p class="testimonials__body">Marisol was extremely helpful during the entire process. Moving to another country is a very challenging ordeal and having someone like Marisol on your side makes all the difference. She’s continued to be incredibly helpful even after arriving, fielding every one of my questions and following up with helpful suggestions. She has been a critical part of the process!</p>
    <div class="testimonials__dots">
      <span class="testimonials__dot testimonials__dot--active"></span>
      <span class="testimonials__dot"></span>
      <span class="testimonials__dot"></span>
      <span class="testimonials__dot"></span>
      <span class="testimonials__dot"></span>
    </div>
  </section>

  <section class="faq-band" role="img" aria-label="Photo of a giant carved stone Buddha face among green trees">
    <p class="faq-band__text">Read frequently asked questions about our program..</p>
    <a class="faq-band__button" href="#">READ MORE</a>
  </section>
</body>
</html>
```